Halden & Pruitt Periodontics and Implant Solutions Business Card

We are a specialty dental practice- implants and periodontal surgery. We have just re-designed our logo and are building a new office and would like to re-design our business card. We are looking for something professional with a creative and artsy twist- something to stand out among the rest! Happy Designing!

I have uploaded all versions of our new logo and our current business card. We have 3 locations and 2 doctors.

Target Market(s)

55+

Industry/Entity Type

Dental

Contact Information for Business Card

Needs Names, logo, locations- professional and artsy!

Colors
0555a3
0592cd
34a7d7
3277b5
85cae6
85acd3
cee9f5
ecf7fb

Requirements
Must have
• our names:
• Thomas E. Halden D.M.D.
• Celia M. Pruitt D.M.D.
• Diplomate of the National Council of Gum Surgery
• Address locations:
• 462 W. Larkspur Avenue Suite 210B Plantation, FL 33871
• Tel: 954-318-2264 Fax: 954-318-2291
• 5127 Harlow Lane #C-4 Boca Raton, FL 33609
• Tel: 561-627-1958 Fax: 561-703-2816
• 274 Northwest 9th Street #412 Miami FL 33987
• Tel: 786-429-6153 Fax: 786-429-6170
Nice to have
• unique look
Should not have
• doesn't need QR like our current card has.

```html
<!DOCTYPE html>
<html lang="en">
<head>
<meta charset="utf-8">
<title>Halden &amp; Pruitt Business Card</title>
<link rel="stylesheet" href="https://fonts.googleapis.com/css2?family=Questrial&family=Roboto+Condensed:wght@300;700&display=swap">
<style>
  :root {
    --backdrop: #1e1f22;
    --navy: #262f78;
    --navy-deep: #1d2566;
    --navy-light: #2f3a8a;
    --paper: #f4f4f2;
    --curve-shadow: #7b7c80;
    --ink-navy: #232d73;
    --text-light: #e9ebf4;
    --text-soft: #c9cde2;
    --divider: rgba(255,255,255,0.28);
  }
  html, body {
    margin: 0;
    padding: 0;
    width: 1200px;
    height: 1001px;
    overflow: hidden;
    background: var(--backdrop);
  }
  .stage {
    position: relative;
    width: 1200px;
    height: 1001px;
  }
  .card {
    position: absolute;
    left: 306px;
    width: 588px;
    height: 330px;
    overflow: hidden;
    background: linear-gradient(160deg, var(--navy-light) 0%, var(--navy) 45%, var(--navy-deep) 100%);
  }
  .card--front { top: 133px; }
  .card--back  { top: 540px; }

  .front-curve {
    position: absolute;
    inset: 0;
    width: 588px;
    height: 330px;
  }
  .brand {
    position: absolute;
    font-family: "Questrial", sans-serif;
    font-weight: 400;
    white-space: nowrap;
  }
  .brand__name { display: block; letter-spacing: -0.5px; }
  .brand__tagline { display: block; }

  .card--front .brand {
    left: 40px;
    top: 152px;
    color: var(--ink-navy);
  }
  .card--front .brand__name { font-size: 27px; line-height: 30px; }
  .card--front .brand__tagline { font-size: 12.5px; line-height: 16px; margin-top: 1px; }

  .doctor {
    position: absolute;
    right: 38px;
    margin: 0;
    font-family: "Roboto Condensed", sans-serif;
    font-weight: 700;
    font-size: 23px;
    color: var(--text-soft);
    white-space: nowrap;
  }
  .doctor--first { top: 42px; }
  .doctor--second { top: 258px; }

  .credential {
    position: absolute;
    left: 340px;
    width: 210px;
    top: 132px;
    margin: 0;
    text-align: center;
    font-family: "Questrial", sans-serif;
    font-size: 16.5px;
    line-height: 21px;
    color: var(--text-light);
  }

  .card--back .brand {
    left: 32px;
    top: 98px;
    color: var(--text-light);
  }
  .brand-dot {
    position: absolute;
    left: 32px;
    top: 96px;
    width: 64px;
    height: 64px;
    border-radius: 50%;
    border: 3px solid var(--text-light);
    box-sizing: border-box;
  }
  .card--back .brand { left: 110px; top: 100px; }
  .card--back .brand__name { font-size: 30px; line-height: 34px; }
  .card--back .brand__tagline { font-size: 13px; line-height: 16px; }

  .locations {
    position: absolute;
    left: 30px;
    right: 20px;
    top: 234px;
    display: flex;
  }
  .location {
    font-family: "Roboto Condensed", sans-serif;
    font-weight: 300;
    font-size: 13.5px;
    line-height: 16.3px;
    color: var(--text-light);
    font-style: normal;
    white-space: nowrap;
  }
  .location--one { width: 190px; }
  .location--two, .location--three {
    border-left: 1px solid var(--divider);
    padding-left: 25px;
  }
  .location--two { width: 148px; }
</style>
</head>
<body>
<main class="stage">

  <section class="card card--front" aria-label="Business card front">
    <svg class="front-curve" viewBox="0 0 588 330" aria-hidden="true">
      <path d="M0 0 H262 C318 70 330 230 206 330 H0 Z" fill="var(--curve-shadow)"/>
      <path d="M0 0 H252 C305 70 318 220 254 330 H0 Z" fill="var(--curve-shadow)" opacity="0"/>
      <path d="M0 0 H252 C300 60 316 200 204 330 H0 Z" fill="var(--paper)"/>
    </svg>
    <div class="brand">
      <span class="brand__name">HALDEN &amp; PRUITT</span>
      <span class="brand__tagline">Periodontics and Implant Solutions</span>
    </div>
    <h2 class="doctor doctor--first">Thomas E. Halden D.M.D.</h2>
    <p class="credential">Diplomate of the National Council of Gum Surgery</p>
    <h2 class="doctor doctor--second">Celia M. Pruitt D.M.D.</h2>
  </section>

  <section class="card card--back" aria-label="Business card back">
    <span class="brand-dot" aria-hidden="true"></span>
    <div class="brand">
      <span class="brand__name">HALDEN &amp; PRUITT</span>
      <span class="brand__tagline">Periodontics and Implant Solutions</span>
    </div>
    <div class="locations">
      <address class="location location--one">
        462 W. Larkspur Avenue<br>
        Suite 210B Plantation, FL 33871<br>
        Tel: 954-318-2264<br>
        Fax: 954-318-2291
      </address>
      <address class="location location--two">
        5127 Harlow Lane #C-4<br>
        Boca Raton, FL 33609<br>
        Tel: 561-627-1958<br>
        Fax: 561-703-2816
      </address>
      <address class="location location--three">
        274 Northwest 9th Street<br>
        #412 Miami FL 33987<br>
        Tel: 786-429-6153<br>
        Fax: 786-429-6170
      </address>
    </div>
  </section>

</main>
</body>
</html>
```